FlockVault.net website design

We are looking for a design for a new website we are about to launch called FlockVault.net. FlockVault.net is an online discount wine site that will focus on selling only one wine at a time. (This potentially may become two or three wines at a time in the future but only one for now). The wine that is up for sale will not actually be sold until a pre-set number of buyers “the group” commits to buying the wine. If the threshold of buyers is not met then the wine is not sold. This group aspect is what makes the site unique. By only selling the wine when the group commits to buying it we are able to deliver them a great wine at a fantastic price.
The website should convey a fun feeling while also indicating that this is a place where serious wine enthusiasts can shop. We will be providing information, ratings, and reviews about the wines that are currently on sale.
Updates
Target Market(s)
The target market is a wide range of wine enthusiasts, from people in their 20s and 30s to more mature and serious wine connoisseurs.
Industry/Entity Type
Shop
Requirements
Must have
- Below is a list of specifications for the website:
1) Main page with our logo (which includes green, purple, and a magenta wine color) that showcases the current wine that's for sale
- The site’s main focus should be on selling ONE bottle of wine at a time at group rate.
- The site should capture the group buying concept as this is what differentiates our site from the others. Visitors to the site should get the sense that they are part of a special community that is getting a great deal because they are buying the wine as a group.
- A meter or better yet an animation should be used to indicate if the tipping point has been met for a sale. We’d like to see some creative ideas here.
- Nice high-res photo of the wine bottle
- Detailed description of what kind of wine it is, where the wine is from, type of grape, vino observer and other ratings, description of what it tastes like. We would like the option to provide as much detail here as possible.
- Breakdown on what the prices are per bottle and the discount we're giving. We would like to show the original price as compared to the FlockVault.net price.
- Potentially show a list of upcoming wines. Maybe not the exact wine that will be for sale next but some info to entice users to keep checking.
2) User Account Log in
- Ability to create and log into a personal account
The personal account should be able to:
-store users' credit card and shipping information as well as past orders
-allow you to opt in or out of flock vault emails
-potentially store wine preference or ratings information
-refer a friend option where you get some kind of incentive
3) The Group Concept. The website design must include a few aspects that identify FlockVault.net as a social site, not simply a wine sale site.
- Some kind of indicator showing if the group threshold has been met or not. We would like to see some type of animation with wine bottles filling up, or grapes on a scale-something that would change as the number of people buying into the sale increase.
- Button to join the group purchase
4) General Site Content must include:
- Email link to send questions to support
- Information on how shipping works and other FAQs
- Legal disclaimer
- Links to Facebook and Twitter
Nice to have
- It would be nice to have a discussion board where FlockVault members can discuss wines.
Should not have
- The design should not be for a general wine store that sells a variety of different wines.

```html
<!DOCTYPE html>
<html lang="en">
<head>
<meta charset="utf-8">
<title>FlockVault.net</title>
<link rel="stylesheet" href="https://fonts.googleapis.com/css2?family=Lobster&family=Great+Vibes&family=Merriweather:wght@400;700&family=Droid+Serif&display=swap">
<style>
:root{
  --paper:#f7f2ea;
  --hero-light:#f7a04c;
  --hero-mid:#e2642a;
  --hero-dark:#8a2a12;
  --band-dark:#5a1e12;
  --ink:#3a1a0e;
  --magenta:#a8336a;
  --green:#7fae2a;
  --wood-1:#a4471a;
  --wood-2:#b5541f;
  --wood-3:#93401a;
  --wood-edge:#6b2a10;
  --cream:#fff4e6;
  --button:#e08a36;
  --button-dark:#b0601c;
  --footer:#5c2a12;
  --footer-2:#4b200c;
  --stripe:#d9d1c9;
}
*{box-sizing:border-box;margin:0;padding:0}
html,body{width:690px;height:1200px;overflow:hidden;background:#fff}
.canvas{position:relative;width:690px;height:1200px;overflow:hidden;font-family:'Merriweather',Georgia,serif;color:var(--ink)}
.abs{position:absolute}
.nowrap{white-space:nowrap}

/* header */
.site-header{left:0;top:0;width:690px;height:44px;background:var(--paper);border-bottom:3px solid #e7a6a0}
.brand{left:76px;top:9px;display:flex;align-items:center;gap:6px}
.brand-dot{width:22px;height:22px;border-radius:50%;background:var(--magenta)}
.brand-name{font-weight:700;font-size:17px;color:var(--green)}
.main-nav{left:229px;top:0;height:44px;display:flex}
.nav-item{height:44px;padding:5px 10px 0;border-left:1px dashed #bdb3a6;text-align:center}
.nav-item:last-child{border-right:1px dashed #bdb3a6}
.nav-item .label{display:block;font-family:'Droid Serif',Georgia,serif;font-size:14px;color:#333;line-height:16px}
.nav-item .sub{display:block;font-family:'Lobster',cursive;font-size:10px;color:var(--magenta);line-height:14px}
.nav-item .sub.is-green{color:var(--green)}

/* hero */
.hero{left:0;top:44px;width:690px;height:278px;background:radial-gradient(ellipse 360px 230px at 330px 120px,var(--hero-light),var(--hero-mid) 55%,var(--hero-dark) 100%)}
.hero-visual{left:500px;top:14px;width:92px;height:190px;border-radius:10px;background:linear-gradient(160deg,#2b1a1e,#7a1222 55%,#4a2c5a)}
.hero-grapes{left:456px;top:168px;width:98px;height:72px;border-radius:50%;background:radial-gradient(circle at 45% 45%,#6a5a8a,#3a2a50 70%)}
.hero-kicker{left:163px;top:30px;font-family:'Lobster',cursive;font-size:28px;color:var(--band-dark)}
.hero-band{left:111px;top:76px;width:385px;height:46px;background:rgba(120,35,12,.75);border-top:1px solid rgba(255,200,150,.4);border-bottom:1px solid rgba(255,200,150,.4)}
.hero-title{left:111px;top:74px;width:385px;text-align:center;font-family:'Great Vibes',cursive;font-weight:400;font-size:40px;line-height:48px;color:#fff;text-shadow:1px 1px 0 #3a0c00}
.rating{left:416px;top:116px}
.hero-lead{left:163px;top:142px;font-size:13px;color:var(--band-dark)}
.hero-price{left:440px;top:144px;font-family:'Lobster',cursive;font-size:30px;color:#5a1408}
.hero-quote{left:163px;top:188px;width:280px;font-size:8.5px;line-height:12px;color:var(--band-dark)}

/* deal meter */
.deal{left:0;top:0;width:690px;height:1px}
.deal-band{left:0;top:322px;width:690px;height:88px;background:repeating-linear-gradient(90deg,var(--stripe) 0 2px,#e6dfd8 2px 5px)}
.deal-strip{left:0;top:340px;width:690px;height:44px;background:#fff;border-top:1px solid #ccc;border-bottom:1px solid #ccc}
.deal-count{left:140px;top:342px;font-family:'Lobster',cursive;font-size:18px;line-height:22px;color:var(--magenta)}
.deal-rest{left:207px;top:366px;font-size:13px;line-height:16px;color:#222}
.deal-visual{left:355px;top:312px;width:165px;height:72px;background:linear-gradient(90deg,#6a0f14,#7a1420 45%,#1e1c24);border-radius:4px 4px 0 0}

/* tabs */
.tab-row{left:0;top:410px;width:690px;height:44px;background:var(--paper);border-top:3px solid #e7a6a0}
.tab{top:413px;height:41px;padding:6px 16px 0 10px;background:#fff;border-left:1px dashed #bdb3a6;border-right:1px dashed #bdb3a6;display:flex;gap:5px}
.tab .label{display:block;font-family:'Droid Serif',Georgia,serif;font-size:13px;color:#333;line-height:15px}
.tab .sub{display:block;font-family:'Lobster',cursive;font-size:10px;color:var(--magenta);text-align:right}
.tab .sub.is-green{color:var(--green)}

/* wood content */
.content{left:0;top:454px;width:690px;height:606px;background:
  repeating-linear-gradient(0deg,rgba(0,0,0,.05) 0 1px,transparent 1px 7px),
  linear-gradient(90deg,var(--wood-3),var(--wood-2) 30%,var(--wood-1) 60%,var(--wood-2) 85%,var(--wood-3))}
.row{position:absolute;left:0;width:690px;height:303px;border-bottom:2px solid var(--wood-edge)}
.row-divider{left:352px;top:0;width:1px;height:303px;background:var(--wood-edge);box-shadow:1px 0 0 rgba(255,200,150,.2)}
.col-heading{font-family:'Lobster',cursive;font-weight:400;font-size:15px;color:var(--cream);white-space:nowrap}
.body-text{font-size:8px;line-height:11.5px;color:var(--cream)}
.thumb{border:2px solid #fff;border-radius:1px}
.thumb.is-feature{background:linear-gradient(135deg,#2a1206,#c98a2a 50%,#5a1414)}
.thumb.is-barrel{background:linear-gradient(135deg,#1a0e08,#7a4a22 55%,#1a0e08)}
.btn{display:block;width:62px;height:17px;border-radius:3px;background:linear-gradient(var(--button),var(--button-dark));border:1px solid #7a3a10;font-family:'Lobster',cursive;font-size:10px;color:#4a1e06;text-align:center;line-height:15px}
.feature-text{left:75px;top:50px;width:265px}
.feature-text .thumb{float:left;width:90px;height:66px;margin:0 8px 4px 0}

/* footer */
.site-footer{left:0;top:1060px;width:690px;height:140px;background:linear-gradient(var(--footer),var(--footer-2));border-top:2px solid #3a1606}
.footer-col{top:14px;width:88px;color:var(--cream)}
.footer-col h3{font-family:'Lobster',cursive;font-weight:400;font-size:13px;line-height:14px;margin-bottom:6px}
.footer-col li{list-style:none;font-size:8.5px;line-height:15.5px}
.footer-col .bullets li{font-size:7.5px;line-height:11.5px;padding-left:9px;position:relative}
.footer-col .bullets li::before{content:"›";position:absolute;left:0;color:#f0c08a}
.footer-col .bullets.loose li{margin-bottom:6px}
.footer-col p{font-size:7.5px;line-height:11.5px;padding-left:6px}
.footer-visual{left:504px;top:1040px;width:54px;height:36px;border-radius:6px;background:linear-gradient(#8ab030,#5a3a1a 60%)}
</style>
</head>
<body>
<div class="canvas">

  <header class="site-header abs">
    <div class="brand abs"><span class="brand-dot"></span><span class="brand-name">FlockVault</span></div>
    <nav class="main-nav abs">
      <div class="nav-item"><span class="label">home page</span><span class="sub is-green">start here</span></div>
      <div class="nav-item"><span class="label">upcoming</span><span class="sub">new wines</span></div>
      <div class="nav-item"><span class="label">our blog</span><span class="sub">writing</span></div>
      <div class="nav-item"><span class="label">community</span><span class="sub">wine lovers</span></div>
      <div class="nav-item"><span class="label">contact</span><span class="sub">talking</span></div>
    </nav>
  </header>

  <section class="hero abs">
    <div class="hero-visual abs" role="img" aria-label="Wine bottle and glass of red wine"></div>
    <div class="hero-grapes abs" role="img" aria-label="Bunch of dark grapes"></div>
    <div class="hero-kicker abs nowrap">Month’s wine...</div>
    <div class="hero-band abs"></div>
    <h1 class="hero-title abs nowrap">Moscato D’Asti</h1>
    <svg class="rating abs" width="66" height="14" viewBox="0 0 66 14" aria-label="5 stars">
      <g fill="#f6c12a" stroke="#b77a10" stroke-width=".6">
        <polygon points="6.5,0.5 8.3,4.8 12.8,5 9.3,7.9 10.5,12.4 6.5,9.8 2.5,12.4 3.7,7.9 0.2,5 4.7,4.8"/>
        <polygon transform="translate(13 0)" points="6.5,0.5 8.3,4.8 12.8,5 9.3,7.9 10.5,12.4 6.5,9.8 2.5,12.4 3.7,7.9 0.2,5 4.7,4.8"/>
        <polygon transform="translate(26 0)" points="6.5,0.5 8.3,4.8 12.8,5 9.3,7.9 10.5,12.4 6.5,9.8 2.5,12.4 3.7,7.9 0.2,5 4.7,4.8"/>
        <polygon transform="translate(39 0)" points="6.5,0.5 8.3,4.8 12.8,5 9.3,7.9 10.5,12.4 6.5,9.8 2.5,12.4 3.7,7.9 0.2,5 4.7,4.8"/>
        <polygon transform="translate(52 0)" points="6.5,0.5 8.3,4.8 12.8,5 9.3,7.9 10.5,12.4 6.5,9.8 2.5,12.4 3.7,7.9 0.2,5 4.7,4.8"/>
      </g>
    </svg>
    <p class="hero-lead abs nowrap">Sed et leo nunc, ut consectetur tellus.</p>
    <div class="hero-price abs nowrap">$30</div>
    <p class="hero-quote abs">“Sed sit amet convallis lorem. Maecenas ac felis elit. Integer suscipit, sapien quis rutrum dapibus, enim diam egestas justo, quis pellentesque velit ipsum at quam. ”</p>
  </section>

  <section class="deal abs">
    <div class="deal-band abs"></div>
    <div class="deal-strip abs"></div>
    <div class="deal-count abs nowrap">332 people already bought</div>
    <div class="deal-rest abs nowrap">more 27 for the deal.</div>
    <div class="deal-visual abs" role="img" aria-label="Row of wine bottles and glasses filling up as buyers join"></div>
  </section>

  <div class="tab-row abs"></div>
  <div class="tab abs" style="left:76px">
    <svg width="16" height="16" viewBox="0 0 16 16"><path d="M4 1h8c0 5-2 7-4 7S4 6 4 1zM8 8v5M5 14h6" fill="none" stroke="#a8336a" stroke-width="1.5"/></svg>
    <div><span class="label nowrap">how it works?</span><span class="sub is-green nowrap">join the cellar!</span></div>
  </div>
  <div class="tab abs" style="left:357px">
    <svg width="16" height="16" viewBox="0 0 16 16"><path d="M4 1h8c0 5-2 7-4 7S4 6 4 1zM8 8v5M5 14h6" fill="none" stroke="#a8336a" stroke-width="1.5"/></svg>
    <div><span class="label nowrap">latest wines</span><span class="sub nowrap">you’ve tasted</span></div>
  </div>

  <main class="content abs">
    <section class="row" style="top:0">
      <div class="row-divider abs"></div>
      <h2 class="col-heading abs" style="left:75px;top:22px">Community buying is cheaper</h2>
      <div class="feature-text abs body-text">
        <div class="thumb is-feature" role="img" aria-label="Wine bottles and glasses"></div>
        Quisque auctor velit ut est mollis sed bibendum magna congue. Aenean vulputate risus mattis lectus vulputate iaculis. Duis sit amet sapien in felis fringilla viverra. Nullam tortor nulla, tristique id mollis fringilla, imperdiet id ipsum. Fusce id tellus ligula. Phasellus non felis nec sodales massa faucibus tempor non quis mauris. Integer aliquam mauris urna, et fringilla lorem.
      </div>
      <a class="btn abs" style="left:281px;top:153px">join now</a>
      <h2 class="col-heading abs" style="left:75px;top:192px">Nullam imperdiet</h2>
      <p class="body-text abs" style="left:75px;top:220px;width:265px">“Proin vitae hendrerit justo. In ullamcorper, augue ullamcorper consectetur convallis, purus odio vulputate diam, a pulvinar leo mauris nec tristique mollis fringilla matis lectus vulputate ante mirrum quod non verant ante. ”</p>
      <a class="btn abs" style="left:304px;top:271px">view</a>

      <h2 class="col-heading abs" style="left:375px;top:22px">Duis sit amet sapien</h2>
      <div class="thumb is-barrel abs" style="left:375px;top:50px;width:64px;height:52px" role="img" aria-label="Wine bottle by a barrel"></div>
      <p class="body-text abs" style="left:448px;top:50px;width:180px">Duis sit amet sapien in felis fringilla viverra. Nullam tortor nulla, tristique id mollis fringilla, imperdiet id ipsum.</p>
      <a class="btn abs" style="left:584px;top:94px">view</a>
      <div class="thumb is-barrel abs" style="left:375px;top:138px;width:64px;height:52px" role="img" aria-label="Wine bottle by a barrel"></div>
      <p class="body-text abs" style="left:448px;top:138px;width:180px">Duis sit amet sapien in felis fringilla viverra. Nullam tortor nulla, tristique id mollis fringilla, imperdiet id ipsum.</p>
      <a class="btn abs" style="left:584px;top:182px">view</a>
      <div class="thumb is-barrel abs" style="left:375px;top:225px;width:64px;height:52px" role="img" aria-label="Wine bottle by a barrel"></div>
      <p class="body-text abs" style="left:448px;top:225px;width:180px">Duis sit amet sapien in felis fringilla viverra. Nullam tortor nulla, tristique id mollis fringilla, imperdiet id ipsum.</p>
      <a class="btn abs" style="left:584px;top:269px">view</a>
    </section>

    <section class="row" style="top:303px">
      <div class="row-divider abs"></div>
      <h2 class="col-heading abs" style="left:75px;top:22px">Community buying is cheaper</h2>
      <div class="feature-text abs body-text">
        <div class="thumb is-feature" style="width:72px" role="img" aria-label="Wine bottles and glasses"></div>
        Quisque auctor velit ut est mollis sed bibendum magna congue. Aenean vulputate risus mattis lectus vulputate iaculis. Duis sit amet sapien in felis fringilla viverra. Nullam tortor nulla, tristique id mollis fringilla, imperdiet id ipsum. Fusce id tellus ligula. Phasellus non felis nec sodales massa faucibus tempor non quis mauris. Integer aliquam mauris urna, et fringilla lorem.
      </div>
      <a class="btn abs" style="left:281px;top:153px">join now</a>
      <h2 class="col-heading abs" style="left:75px;top:192px">Nullam imperdiet</h2>
      <p class="body-text abs" style="left:75px;top:220px;width:265px">“Proin vitae hendrerit justo. In ullamcorper, augue ullamcorper consectetur convallis, purus odio vulputate diam, a pulvinar leo mauris nec tristique mollis fringilla matis lectus vulputate ante mirrum quod non verant ante. ”</p>
      <a class="btn abs" style="left:304px;top:271px">view</a>

      <h2 class="col-heading abs" style="left:375px;top:22px">Duis sit amet sapien</h2>
      <div class="thumb is-barrel abs" style="left:375px;top:50px;width:64px;height:52px" role="img" aria-label="Wine bottle by a barrel"></div>
      <p class="body-text abs" style="left:448px;top:50px;width:180px">Duis sit amet sapien in felis fringilla viverra. Nullam tortor nulla, tristique id mollis fringilla, imperdiet id ipsum.</p>
      <a class="btn abs" style="left:584px;top:94px">view</a>
      <div class="thumb is-barrel abs" style="left:375px;top:138px;width:64px;height:52px" role="img" aria-label="Wine bottle by a barrel"></div>
      <p class="body-text abs" style="left:448px;top:138px;width:180px">Duis sit amet sapien in felis fringilla viverra. Nullam tortor nulla, tristique id mollis fringilla, imperdiet id ipsum.</p>
      <a class="btn abs" style="left:584px;top:182px">view</a>
      <div class="thumb is-barrel abs" style="left:375px;top:225px;width:64px;height:52px" role="img" aria-label="Wine bottle by a barrel"></div>
      <p class="body-text abs" style="left:448px;top:225px;width:180px">Duis sit amet sapien in felis fringilla viverra. Nullam tortor nulla, tristique id mollis fringilla, imperdiet id ipsum.</p>
      <a class="btn abs" style="left:584px;top:269px">view</a>
    </section>
  </main>

  <footer class="site-footer abs">
    <div class="footer-col abs" style="left:75px">
      <h3>Pages</h3>
      <ul><li>Home</li><li>Upcoming</li><li>Our blog</li><li>Community</li><li>Contact</li></ul>
    </div>
    <div class="footer-col abs" style="left:168px">
      <h3>Last updates</h3>
      <ul class="bullets loose"><li>In hac habitasse platea dictumst. Praesent iaculis</li><li>Faucibus pretium. Nullam dictum viverra augue id</li></ul>
    </div>
    <div class="footer-col abs" style="left:262px">
      <h3>Contact information</h3>
      <p>Our telephones:<br>555018244<br>555092811</p>
    </div>
    <div class="footer-col abs" style="left:356px">
      <h3>Our affiliates</h3>
      <ul class="bullets"><li>Lorem ipsum dolor</li><li>Egestas diam</li><li>Aliquet Hendrerit</li><li>Libero et sudis</li><li>Non potest augue</li><li>Vehicula tempus porta</li></ul>
    </div>
    <div class="footer-col abs" style="left:450px">
      <h3>Erat urna</h3>
      <ul class="bullets"><li>Lorem ipsum dolor</li><li>Egestas diam</li><li>Aliquet Hendrerit</li><li>Libero et sudis Non potest augue</li></ul>
    </div>
    <div class="footer-col abs" style="left:543px">
      <h3>Egestas diam</h3>
      <ul class="bullets"><li>Lorem ipsum dolor</li><li>Egestas diam</li><li>Aliquet Hendrerit</li><li>Libero et sudis Non potest augue</li></ul>
    </div>
  </footer>
  <div class="footer-visual abs" role="img" aria-label="Grapes resting on a small wine barrel"></div>

</div>
</body>
</html>
```